Need a website to promote and sell my book

Using images from the book, I need a website designed that helps promote the book and eventually sell it.
*Need a landing page
*About the author page
*Storefront page to purchase
*Coming soon page
*"Featured in" page that can link to news articles etc.
The images posted here are examples, the winner of the contest will get the images from the finished book. I will provide the exact text to the winner of the contest.

I can also provide images of kids reading the book. For now, I'll just use one, the winner can have them all to choose from.
Updates

Extending deadline to allow for a few more designers to submit and to allow time for me to review and hold a poll

Target Market(s)

Parents, aunts, uncles, grandparents, friends who have kids; teachers, daycare teachers, babysitters etc.

Industry/Entity Type

Custom Publishing

Coding

Coded - Design and coding required

Number of Pages Required

5+ page

Font styles to use
Sans Serif

Colors

Designer to choose colors to be used in the design.

Requirements
Must have
• It must have a fun feel like the book.
Nice to have
• Would be great to have a section that automatically pulls tweets about the book into it.

```html
<!DOCTYPE html>
<html lang="en">
<head>
<meta charset="utf-8">
<title>Maribel Quist, PhD — Exploring Our Science World</title>
<link href="https://fonts.googleapis.com/css2?family=Baloo+2:wght@600;700;800&family=Nunito:wght@400;600;700;800&display=swap" rel="stylesheet">
<style>
:root{
  --purple:#4b2b8f;
  --orange:#f26a3d;
  --orange-dark:#e0552a;
  --coral:#ef5f48;
  --sky:#a9dcf3;
  --sky-light:#d6effa;
  --ink:#3a3a4a;
  --muted:#7a7a88;
  --white:#ffffff;
  --cream:#fdf8f3;
  --social:#3d8fd8;
}
*{box-sizing:border-box;margin:0;padding:0}
html,body{width:1200px;height:2208px;overflow:hidden}
body{font-family:"Nunito",sans-serif;color:var(--ink);background:var(--white);position:relative}
.btn{display:inline-block;background:var(--orange);color:var(--white);font-family:"Nunito",sans-serif;font-weight:800;font-size:18px;padding:12px 34px;border-radius:28px;box-shadow:0 4px 0 var(--orange-dark);text-decoration:none}

/* hero */
.hero{position:absolute;left:0;top:0;width:1200px;height:410px;background:var(--purple)}
.hero-photo{position:absolute;left:150px;top:0;width:430px;height:380px;background:linear-gradient(135deg,#c9a07a,#8d6a9e 60%,#5a3a8f)}
.site-name{position:absolute;left:24px;top:14px;color:var(--white);font-weight:800;font-size:18px}
.nav{position:absolute;right:190px;top:12px;display:flex;gap:24px;list-style:none}
.nav a{color:var(--white);font-size:13px;font-weight:700;text-decoration:none;padding:5px 10px;border-radius:4px}
.nav .active{background:var(--orange)}
.hero-title{position:absolute;left:770px;top:62px;width:400px;color:var(--white);font-family:"Baloo 2",sans-serif;font-size:44px;line-height:1.05;font-weight:800}
.hero-title .hl{color:var(--orange)}
.hero-text{position:absolute;left:770px;top:214px;width:330px;color:#e6ddf7;font-size:15px;line-height:1.45}
.hero .btn{position:absolute;left:770px;top:290px}
.hero-wave{position:absolute;left:0;top:370px;width:1200px;height:50px}

/* about */
.about{position:absolute;left:0;top:420px;width:1200px;height:420px;background:var(--white)}
.section-title{font-family:"Baloo 2",sans-serif;font-weight:800;color:var(--orange);text-align:center;font-size:50px}
.about .section-title{position:absolute;left:0;width:1200px;top:44px}
.about-text{position:absolute;left:350px;width:500px;top:118px;text-align:center;font-size:14px;line-height:1.55;color:var(--muted)}
.about .btn{position:absolute;left:525px;top:205px}
.badge-art{position:absolute;border-radius:50%}
.gallery{position:absolute;left:240px;top:300px;display:flex;gap:12px}
.gallery div{width:171px;height:90px;border-radius:10px}
.divider{position:absolute;left:120px;top:830px;width:960px;height:20px;border-radius:50%;box-shadow:0 10px 14px -10px rgba(0,0,0,.25)}

/* our book */
.book{position:absolute;left:0;top:860px;width:1200px;height:500px;background:var(--cream)}
.book-cover{position:absolute;left:260px;top:80px;width:270px;height:270px;border-radius:4px;background:linear-gradient(160deg,#7cc7ec,#f7c948 55%,#ef7b5a);box-shadow:8px 10px 0 rgba(0,0,0,.12)}
.book-side{position:absolute;left:150px;top:180px;width:120px;height:110px;background:linear-gradient(135deg,#f7a23b,#ef5f48)}
.book-side-right{position:absolute;left:890px;top:340px;width:130px;height:120px;background:linear-gradient(135deg,#ef5f48,#f7c948);transform:rotate(6deg)}
.book .title{position:absolute;left:598px;top:135px;font-family:"Baloo 2",sans-serif;font-weight:800;font-size:50px;color:var(--orange)}
.book .text{position:absolute;left:600px;top:205px;width:320px;font-size:15px;line-height:1.5;color:var(--muted)}
.book .btn{position:absolute;left:600px;top:365px}

/* stats */
.clouds{position:absolute;left:0;top:1330px;width:1200px;height:100px}
.stats{position:absolute;left:0;top:1420px;width:1200px;height:150px;background:var(--sky);display:flex;justify-content:center;gap:110px;padding-top:28px}
.stat{text-align:center;width:110px;color:var(--white)}
.stat strong{display:block;font-family:"Baloo 2",sans-serif;font-size:40px;line-height:1}
.stat span{font-size:12px;font-weight:700}

/* articles */
.articles{position:absolute;left:0;top:1580px;width:1200px;height:380px}
.articles .section-title{position:absolute;left:0;width:1200px;top:20px;color:var(--ink)}
.articles-intro{position:absolute;left:400px;width:400px;top:90px;text-align:center;font-size:15px;line-height:1.5;color:var(--muted)}
.cards{position:absolute;left:268px;top:145px;display:flex;gap:18px}
.card{width:210px}
.card-photo{height:120px;border-radius:10px;margin-bottom:12px}
.card h3{font-size:14px;font-weight:800;line-height:1.3;color:var(--ink)}
.card p{font-size:13px;color:var(--muted);margin-top:6px;line-height:1.4}
.card-arrow{margin-top:8px;display:block}

/* footer */
.footer{position:absolute;left:0;top:1960px;width:1200px;height:248px}
.footer-bg{position:absolute;left:0;top:0}
.footer-name{position:absolute;left:0;width:1200px;top:82px;text-align:center;color:var(--white);font-weight:800;font-size:20px}
.socials{position:absolute;left:0;width:1200px;top:122px;display:flex;justify-content:center;gap:14px;list-style:none}
.socials li{width:36px;height:36px;border-radius:50%;background:var(--social)}
.copyright{position:absolute;left:0;width:1200px;top:212px;text-align:center;color:#ffe3dc;font-size:12px}
</style>
</head>
<body>

<header class="hero">
  <div class="hero-photo" role="img" aria-label="Photo of two children reading the science picture book together"></div>
  <div class="site-name">Maribel Quist, PhD</div>
  <ul class="nav">
    <li><a class="active" href="#">Home</a></li>
    <li><a href="#">About</a></li>
    <li><a href="#">Store</a></li>
    <li><a href="#">Coming soon</a></li>
    <li><a href="#">Featured In</a></li>
  </ul>
  <h1 class="hero-title">I had a blast<br>Exploring <span class="hl">Our</span><br><span class="hl">Science</span>World!</h1>
  <p class="hero-text">Stories, simple experiments and bright pictures that make science a joyful game for young readers.</p>
  <a class="btn" href="#">Buy Book</a>
  <svg class="hero-wave" viewBox="0 0 1200 50" preserveAspectRatio="none"><path d="M0 10 Q15 0 30 10 T60 10 T90 10 T120 10 T150 10 T180 10 T210 10 T240 10 T270 10 T300 10 T330 10 T360 10 T390 10 T420 10 T450 10 T480 10 T510 10 T540 10 T570 10 T600 10 T630 10 T660 10 T690 10 T720 10 T750 10 T780 10 T810 10 T840 10 T870 10 T900 10 T930 10 T960 10 T990 10 T1020 10 T1050 10 T1080 10 T1110 10 T1140 10 T1170 10 T1200 10 V50 H0Z" fill="#fff"/></svg>
</header>

<section class="about">
  <div class="badge-art" style="left:120px;top:0;width:110px;height:110px;background:linear-gradient(135deg,#5ec5ef,#f7c948)" role="img" aria-label="Round illustrated badge from the book"></div>
  <div class="badge-art" style="left:880px;top:150px;width:110px;height:100px;border-radius:14px;background:linear-gradient(135deg,#ef5f48,#f7c948)" role="img" aria-label="Illustrated sign from the book"></div>
  <h2 class="section-title">About Our Book</h2>
  <p class="about-text">A playful picture book that invites curious kids to mix, measure and wonder about the tiny things that build our world, one small discovery per page.</p>
  <a class="btn" href="#">Read More</a>
  <div class="gallery">
    <div role="img" aria-label="Photo of a child reading the book" style="background:linear-gradient(135deg,#b58a6a,#6e5a4e)"></div>
    <div role="img" aria-label="Photo of children looking at the book" style="background:linear-gradient(135deg,#d9a98a,#8a6f9a)"></div>
    <div role="img" aria-label="Photo of a child holding the book" style="background:linear-gradient(135deg,#c7b49a,#7a8a9a)"></div>
    <div role="img" aria-label="Photo of a reading moment at home" style="background:linear-gradient(135deg,#e2c2a2,#9a7a6a)"></div>
  </div>
</section>
<div class="divider"></div>

<section class="book">
  <div class="book-side" role="img" aria-label="Illustrated book page sign"></div>
  <div class="book-cover" role="img" aria-label="Book cover illustration with colourful science characters"></div>
  <h2 class="title">Our Book</h2>
  <p class="text">Bright illustrations and friendly rhymes guide little learners through atoms, bubbles and colour changes. Perfect for bedtime reading, classrooms and curious afternoons at home with family and friends.</p>
  <a class="btn" href="#">Buy Book</a>
  <div class="book-side-right" role="img" aria-label="Illustrated sign from the book"></div>
</section>

<svg class="clouds" viewBox="0 0 1200 100" preserveAspectRatio="none"><path d="M0 60 Q60 30 120 55 Q180 20 250 50 Q320 10 400 45 Q470 25 540 55 Q620 15 700 50 Q780 20 860 52 Q940 8 1020 45 Q1090 20 1150 50 Q1180 40 1200 45 V100 H0Z" fill="var(--sky-light)"/><path d="M0 80 Q80 55 160 78 Q240 50 330 76 Q420 55 500 80 Q590 52 680 78 Q770 55 860 80 Q950 50 1040 76 Q1120 58 1200 72 V100 H0Z" fill="var(--sky)"/></svg>
<section class="stats">
  <div class="stat"><strong>15</strong><span>Fun Experiments</span></div>
  <div class="stat"><strong>32</strong><span>Colourful Pages</span></div>
  <div class="stat"><strong>10</strong><span>Years of Teaching</span></div>
  <div class="stat"><strong>255</strong><span>Happy Readers</span></div>
</section>

<section class="articles">
  <h2 class="section-title">Our Articles</h2>
  <p class="articles-intro">Stories and reviews from readers, teachers and the press about learning science together.</p>
  <div class="cards">
    <article class="card">
      <div class="card-photo" role="img" aria-label="Photo of a child reading at a table" style="background:linear-gradient(135deg,#c9a080,#6e5a6e)"></div>
      <h3>Little chemists at the kitchen table</h3>
      <p>Teachers share how simple experiments keep kids curious.</p>
      <svg class="card-arrow" width="30" height="12" viewBox="0 0 30 12"><path d="M0 6H26M20 1l6 5-6 5" stroke="var(--orange)" stroke-width="2" fill="none"/></svg>
    </article>
    <article class="card">
      <div class="card-photo" role="img" aria-label="Photo of a child with an open book" style="background:linear-gradient(135deg,#d8b898,#8a7a6a)"></div>
      <h3>Why picture books spark big questions</h3>
      <p>Parents explain how bright pages start long conversations.</p>
      <svg class="card-arrow" width="30" height="12" viewBox="0 0 30 12"><path d="M0 6H26M20 1l6 5-6 5" stroke="var(--orange)" stroke-width="2" fill="none"/></svg>
    </article>
    <article class="card">
      <div class="card-photo" role="img" aria-label="Photo of a toddler looking at the book" style="background:linear-gradient(135deg,#b8c0d0,#7a6a8a)"></div>
      <h3>A classroom full of bubbling ideas</h3>
      <p>Daycare staff describe reading sessions that turn into play.</p>
      <svg class="card-arrow" width="30" height="12" viewBox="0 0 30 12"><path d="M0 6H26M20 1l6 5-6 5" stroke="var(--orange)" stroke-width="2" fill="none"/></svg>
    </article>
  </div>
</section>

<footer class="footer">
  <svg class="footer-bg" width="1200" height="248" viewBox="0 0 1200 248" preserveAspectRatio="none"><path d="M0 40 Q150 0 300 30 Q450 60 600 28 Q750 0 900 32 Q1050 60 1200 25 V248 H0Z" fill="var(--coral)"/></svg>
  <div class="footer-name">Maribel Quist, PhD</div>
  <ul class="socials" aria-label="Social links">
    <li></li><li></li><li></li><li></li><li></li>
  </ul>
  <p class="copyright">Maribel Quist, PhD © 2024. All rights reserved.</p>
</footer>

</body>
</html>
```